Halvorsen Partners Business Card

Halvorsen Partners Civil Construction
Dorian Halvorsen
CEO
555-318-4076
Dorian@HalvorsenCivil.example
www.HalvorsenCivil.example
Site Development
Utility Construction
Excavation
48730 County Route 19
Land O' Lakes, FL 34999

Target Market(s)

Construction and government

Industry/Entity Type

Business

Contact Information for Business Card

I want an unique design that make a statement

Number of Pages Required

1 page

Font styles to use
Other font styles liked:

Colors

Designer to choose colors to be used in the design.

Requirements
Must have
• unique design, feel free to modify or change the color of my logo.
Nice to have
• extra design features like spot UV, foil accents, color edges, unique paper, or any thing that would make my card pop.
• I like the feel of the image that I attached

```html
<!DOCTYPE html>
<html lang="en">
<head>
<meta charset="utf-8">
<title>Halvorsen Partners Business Card</title>
<link href="https://fonts.googleapis.com/css2?family=Roboto:wght@400;500&family=Roboto+Condensed:wght@500;700&display=swap" rel="stylesheet">
<style>
  :root {
    --backdrop: #262626;
    --paper: #f2f2f2;
    --navy: #1f3c7a;
    --ink: #4a4a4a;
    --white: #ffffff;
  }
  * { margin: 0; padding: 0; box-sizing: border-box; }
  html, body { width: 1200px; height: 960px; overflow: hidden; }
  body {
    background: var(--backdrop);
    position: relative;
    font-family: "Roboto", Arial, sans-serif;
  }
  .card {
    position: absolute;
    width: 600px;
    height: 342px;
    box-shadow: 0 3px 8px rgba(0,0,0,0.45);
    overflow: hidden;
  }
  .card-front { left: 314px; top: 113px; background: var(--paper); }
  .card-back { left: 311px; top: 472px; background: var(--navy); }

  .brand {
    position: absolute;
    display: flex;
    align-items: center;
    gap: 14px;
  }
  .brand-square {
    width: 56px;
    height: 56px;
    flex: none;
  }
  .brand-name {
    font-family: "Roboto", Arial, sans-serif;
    font-weight: 500;
    text-transform: uppercase;
    letter-spacing: 1.5px;
    line-height: 1.25;
  }
  .brand-name .line-main { display: block; font-size: 23px; }
  .brand-name .line-sub { display: block; font-size: 14.5px; letter-spacing: 3.2px; }

  .card-front .brand { left: 51px; top: 56px; }
  .card-front .brand-square { background: var(--navy); }
  .card-front .brand-name { color: var(--navy); }

  .card-back .brand { left: 129px; top: 133px; }
  .card-back .brand-square { background: var(--white); width: 60px; height: 60px; }
  .card-back .brand-name { color: var(--white); }
  .card-back .brand-name .line-main { font-size: 25px; }
  .card-back .brand-name .line-sub { font-size: 15.5px; }

  .contact-list {
    position: absolute;
    left: 51px;
    top: 195px;
    list-style: none;
    font-size: 14px;
    color: var(--ink);
  }
  .contact-list li {
    display: flex;
    align-items: center;
    gap: 8px;
    height: 19.5px;
  }
  .contact-list svg { width: 13px; height: 13px; fill: var(--navy); flex: none; }

  .person {
    position: absolute;
    right: 51px;
    top: 202px;
    text-align: right;
  }
  .person-name {
    font-family: "Roboto Condensed", Arial Narrow, sans-serif;
    font-weight: 700;
    font-size: 21px;
    color: var(--navy);
    text-transform: uppercase;
    line-height: 1.1;
  }
  .person-role {
    font-size: 14px;
    color: var(--ink);
    margin-top: 2px;
  }

  .services-band {
    position: absolute;
    left: 0;
    top: 292px;
    width: 100%;
    height: 29px;
    background: var(--navy);
    color: var(--white);
    font-size: 14.5px;
    display: flex;
    justify-content: center;
    align-items: center;
    gap: 7px;
  }
  .services-band .divider {
    width: 6px; height: 6px; background: var(--white);
  }
</style>
</head>
<body>
  <section class="card card-front">
    <div class="brand">
      <span class="brand-square"></span>
      <span class="brand-name">
        <span class="line-main">Halvorsen Partners</span>
        <span class="line-sub">Civil Construction</span>
      </span>
    </div>

    <ul class="contact-list">
      <li>
        <svg viewBox="0 0 24 24" aria-hidden="true"><path d="M6.6 10.8a15.1 15.1 0 0 0 6.6 6.6l2.2-2.2a1 1 0 0 1 1-.25 11.4 11.4 0 0 0 3.6.57 1 1 0 0 1 1 1V20a1 1 0 0 1-1 1A17 17 0 0 1 3 4a1 1 0 0 1 1-1h3.5a1 1 0 0 1 1 1c0 1.25.2 2.45.57 3.57a1 1 0 0 1-.25 1z"/></svg>
        555-318-4076
      </li>
      <li>
        <svg viewBox="0 0 24 24" aria-hidden="true"><path d="M2 5h20v14H2z M2 5l10 7 10-7" fill="var(--navy)"/><path d="M3 6l9 6.3L21 6" fill="none" stroke="#f2f2f2" stroke-width="1.6"/></svg>
        Dorian@HalvorsenCivil.example
      </li>
      <li>
        <svg viewBox="0 0 24 24" aria-hidden="true"><circle cx="12" cy="12" r="10"/><path d="M2 12h20M12 2c3 3 3 17 0 20M12 2c-3 3-3 17 0 20" fill="none" stroke="#f2f2f2" stroke-width="1.4"/></svg>
        www.HalvorsenCivil.example
      </li>
    </ul>

    <div class="person">
      <div class="person-name">Dorian Halvorsen</div>
      <div class="person-role">CEO</div>
    </div>

    <div class="services-band">
      <span>Site Development</span>
      <span class="divider"></span>
      <span>Utility Construction</span>
      <span class="divider"></span>
      <span>Excavation</span>
    </div>
  </section>

  <section class="card card-back">
    <div class="brand">
      <span class="brand-square"></span>
      <span class="brand-name">
        <span class="line-main">Halvorsen Partners</span>
        <span class="line-sub">Civil Construction</span>
      </span>
    </div>
  </section>
</body>
</html>
```